Law Firm Logo and Stationary

I need a logo for my law firm.  The logo should only contain the firm name "Harlow & Harlow, P.C." but we are open to slight additions like underlining or a box.  We are looking for a modern style but not edgy because our target market is businesses and corporations.

I would like a logo that invokes the traditional values of a law firm (trust, integrity, knowledge) but I want an updated look.

To be clear, the logo should only contain the firm name, I am just looking for a font treatment.

The logo color is up to you.  The only initial opinion I have is that bright colors may not fit with the professional look of a law firm. 

I also want to incorporate the new logo into letterhead and business card designs.  The letterhead should include all of the information that is in my current letterhead, which is attached.  The letterhead should be black or grey on white.  The colored logo will go on the website and promotional materials.

For the business card, I would like to have the logo on the top left, the employee name (Colin J. Harlow) on the middle left and the firm information (address, tel, fax, website, email) on right side.  I am open to suggestions if you have better ideas.
Updates

Here are some comments on the initial 8 designs:

a) I am just interested in a font treatment of our firm name, "Harlow & Harlow, P.C."  I do not want any graphics like a gavel or shield. 

b) The full name of the firm must be in the logo.  So I cannot use designs that only have "H & H"

c) EXAMPLES: Here are two websites with examples of law firm logos that just have the firm name.  These are just samples to give you a general idea of what I am looking for.  Check out:  www.qx-legalco.com and www.tarrowmeade-law.com 

In short, I am looking for a simple, clean design that will look modern enough for our website but is also conservative enough to be on letterhead that gets sent to judges and other lawyers.

Also, the sample letterhead is now loaded in the brief so you can see the information I need included in the new letterhead.

Thanks.

Target Market(s)

businesses and corporations.

Industry/Entity Type

Law Firm

Logo Text

Harlow & Harlow, P.C.

Requirements
Must have
• Firm name, "Harlow & Harlow, P.C."

```html
<!DOCTYPE html>
<html lang="en">
<head>
<meta charset="utf-8">
<title>Harlow &amp; Harlow, P.C. — Identity</title>
<link href="https://fonts.googleapis.com/css2?family=Arimo:wght@400;700&display=swap" rel="stylesheet">
<style>
  :root {
    --bg: #fc7f7d;
    --teal: #007f80;
    --teal-card: #10847f;
    --accent: #3b62e0;
    --muted-square: #558a7c;
  }
  html, body { margin: 0; padding: 0; overflow: hidden; }
  body { width: 1030px; height: 1200px; background: var(--bg); position: relative;
         font-family: "Arimo", Arial, sans-serif; color: var(--teal); }
  .abs { position: absolute; }

  .wordmark { display: flex; align-items: center; white-space: nowrap; }
  .wordmark .mark { background: var(--accent); flex: none; }
  .wordmark .name { font-weight: 700; color: var(--teal); }

  .hero-mark { left: 27px; top: 30px; }
  .hero-mark .mark { width: 52px; height: 52px; margin-right: 20px; }
  .hero-mark .name { font-size: 36px; letter-spacing: 8px; }

  .letterhead { left: 27px; top: 158px; width: 780px; height: 1010px;
                border: 1px solid var(--teal); }
  .letterhead .band { left: 0; top: 0; width: 40px; height: 100%; background: var(--teal); }
  .lh-label { left: 78px; top: 26px; font-size: 13.5px; }
  .lh-mark { left: 78px; top: 53px; }
  .lh-mark .mark { width: 24px; height: 24px; background: var(--teal); margin-right: 11px; }
  .lh-mark .name { font-size: 20px; letter-spacing: 5px; }
  .lh-roster { right: 29px; top: 50px; text-align: right; font-size: 13.5px; line-height: 17px; }
  .lh-roster p { margin: 0 0 17px; }
  .lh-footer { left: 78px; top: 908px; font-size: 13.5px; line-height: 17px; }
  .lh-footer p { margin: 0 0 17px; }
  .sep { padding: 0 7px; }

  .card-front { left: 682px; top: 496px; width: 322px; height: 184px;
                border: 1px solid var(--teal); background: var(--bg); overflow: hidden; }
  .card-front .band { left: 0; top: 0; width: 19px; height: 100%; background: var(--teal); }
  .cf-person { left: 38px; top: 14px; font-size: 9.5px; line-height: 12px; }
  .cf-mark { left: 38px; top: 84px; }
  .cf-mark .mark { width: 18px; height: 18px; margin-right: 8px; }
  .cf-mark .name { font-size: 13px; letter-spacing: 2.5px; }
  .cf-contact { left: 38px; top: 148px; font-size: 9.5px; line-height: 13px; }
  .cf-contact .sep { padding: 0 4px; }

  .card-back { left: 682px; top: 726px; width: 322px; height: 184px; background: var(--teal-card); }
  .card-back .panel { left: 212px; top: 72px; width: 88px; height: 88px; background: var(--muted-square); }
</style>
</head>
<body>

  <div class="abs wordmark hero-mark">
    <span class="mark"></span><span class="name">HARLOW &amp; HARLOW PC</span>
  </div>

  <section class="abs letterhead">
    <div class="abs band"></div>
    <div class="abs lh-label">LAW OFFICES</div>
    <div class="abs wordmark lh-mark">
      <span class="mark"></span><span class="name">HARLOW &amp; HARLOW PC</span>
    </div>
    <div class="abs lh-roster">
      <p>MARTIN E. HARLOW†#<br>COLIN J. HARLOW†*<br>SAMUEL HARLOW (1916-1994)</p>
      <p>ADMITTED TO PRACTICE<br>†District of Columbia<br>#Maryland<br>*New York</p>
    </div>
    <div class="abs lh-footer">
      <p>Writer’s email<br>martin.harlow@harlowpc.com</p>
      <p>Harlow &amp; Harlow, P.C.<span class="sep">|</span>2150 Alder Avenue<span class="sep">|</span>Easton, MD 21601<br>
      t. 301.555.0142&nbsp;&nbsp;&nbsp;&nbsp;f. 301.555.0178&nbsp;&nbsp;&nbsp;&nbsp;www.harlowpc.com</p>
    </div>
  </section>

  <section class="abs card-front">
    <div class="abs band"></div>
    <div class="abs cf-person">Martin E. Harlow<br>martin.harlow@harlowpc.com</div>
    <div class="abs wordmark cf-mark">
      <span class="mark"></span><span class="name">HARLOW &amp; HARLOW PC</span>
    </div>
    <div class="abs cf-contact">2150 Alder Avenue<span class="sep">|</span>Easton, MD 21601<br>
      t. 301.555.0142<span class="sep">|</span>f. 301.555.0178<span class="sep">|</span>www.harlowpc.com</div>
  </section>

  <section class="abs card-back">
    <div class="abs panel"></div>
  </section>

</body>
</html>
```